Zielgruppe
Wir sind eine Event-Agentur im Westen Berlins mit dem Teilschwerpunkt 'Medizin'. Zu unseren Kunden gehören namenhafte Krankenhäuser, Ärzte und Organisationen welche Fortbildungsveranstaltungen bei uns organisieren lassen. Unsere Zielgruppe sind Ärzte und medizinisches Personal, welche an unseren Events teilnehmen um auf dem neusten Stand der Medizin, Hygiene und anderen Themen zu bleiben.
Aufgabenstellung
UPDATE: Unser Chef wünscht sich, dass der Fokus nicht nur auf dem Thema Arthroskopie liegt, sondern schon eher in Richtung 'Gelenke' gehen soll. Bitte entsprechend beachten!
Wir benötigen ein Design für einen DIN lang Flyer, welches gleichzeitig modern und doch nicht zu flippig ist. Das Design muss den Spagat zwischen Technik und Menschlichkeit widerspiegeln. Farblich sind keine Vorgaben vorhanden. Ob mit Stock Fotos, graphischen Elementen oder mit typographischem Design: wir sind für alle Vorschläge offen.
Thematisch geht es um die Bewerbung einer Veranstaltung im orthopädischen Sektor (falls für Ihr Design relevant: es handelt sich um Arthroskopien). Das Design soll so angelegt sein, dass es im nächsten Jahr abgewandelt wiederverwendet werden kann ohne dass der Wiedererkennungswert verloren geht.
Folgende Texte müssen vorhanden sein:
'Veltrana-Symposium 2019' (Name der Veranstaltung)
'Neues aus der Schulter- und Kniearthroskopie' (Thema der Veranstaltung)
'21. bis 23. Februar 2019' (Datum)
'Krankenhaus Berlin' (Ort, leider noch mit Platzhalter)
Nice To Have, aber kein Muss: die Jahreszahl des jeweiligen Jahres könnte immer an der gleichen Stelle erscheinen. Für die nächste VA stünde dort 2019, aber für das darauffolgende Jahr 2020. Allerdings nur ein Gedanke von uns und kein Pflichtelement. Lieber nicht nutzen, falls es das Design irgendwie beeinträchtigt.
Falls Stockbilder dann bitte im erschwinglichen Rahmen vorschlagen! Das schönste Bild hilft uns nicht wenn es 50€ für 200x200 px kostet ;)
Vielen Dank im Voraus für Ihre Vorschläge!

```html
<!DOCTYPE html>
<html lang="de">
<head>
<meta charset="utf-8">
<title>Veltrana-Symposium – DIN-lang-Flyer</title>
<link href="https://fonts.googleapis.com/css2?family=Fira+Sans:wght@300;400;600;700&display=swap" rel="stylesheet">
<style>
  :root {
    --stage: #c4c4c4;
    --paper: #ffffff;
    --ink: #1f2a6e;
    --navy-deep: #0b1a4a;
    --navy-mid: #1b3c9c;
    --navy-glow: #2f8fd8;
  }
  html, body {
    margin: 0;
    padding: 0;
    width: 1200px;
    height: 1200px;
    overflow: hidden;
    background: var(--stage);
    font-family: "Fira Sans", Arial, sans-serif;
  }
  .stage { position: relative; width: 1200px; height: 1200px; }

  .flyer {
    --accent: #0ea6b4;
    --warm: #f59c0d;
    --split: 356px;
    position: absolute;
    width: 522px;
    height: 1044px;
    background: var(--paper);
    overflow: hidden;
    transform-origin: top left;
  }
  .flyer--2019 { left: 52px; top: 78px; }
  .flyer--2020 {
    --accent: #0aa6e4;
    --warm: #f08b1d;
    --split: 355px;
    left: 702px;
    top: 215px;
    transform: scale(0.7663);
  }

  .flyer__shapes { position: absolute; inset: 0; width: 522px; height: 1044px; }
  .shape-accent { fill: var(--accent); }
  .shape-warm { fill: var(--warm); }

  .flyer__date {
    position: absolute; left: 14px; top: 17px; margin: 0;
    font-size: 29px; font-weight: 600; color: var(--warm); line-height: 1.1;
  }
  .flyer__year {
    position: absolute; left: 12px; top: 44px; margin: 0;
    font-size: 62px; font-weight: 600; color: var(--accent); line-height: 1.1;
  }
  .flyer__title {
    position: absolute; left: 18px; top: 752px; margin: 0;
    font-size: 50px; font-weight: 600; color: #fff; line-height: 50px;
    letter-spacing: 0.5px;
  }
  .flyer__topic {
    position: absolute; right: 17px; top: 856px; margin: 0;
    text-align: right; font-size: 20px; line-height: 24px;
  }
  .flyer__topic-lead { display: block; font-weight: 600; color: var(--warm); }
  .flyer__venue { display: block; font-weight: 300; color: var(--accent); }
  .flyer__body {
    position: absolute; right: 17px; top: 937px; width: 490px; margin: 0;
    text-align: right; font-size: 12.3px; line-height: 16px; color: var(--ink);
  }
  .flyer__contact {
    position: absolute; right: 19px; top: 1005px; margin: 0;
    font-size: 17.5px; font-weight: 300; color: var(--accent); letter-spacing: 0.3px;
    display: flex; align-items: center; gap: 5px;
  }
  .flyer__phone { color: var(--warm); }
  .flyer__phone-icon { width: 17px; height: 15px; fill: var(--accent); }
  .flyer__strip {
    position: absolute; left: 0; bottom: 0; width: 100%; height: 11px;
    background: linear-gradient(to right, var(--accent) var(--split), var(--warm) var(--split));
  }
</style>
</head>
<body>
<div class="stage">

  <svg width="0" height="0" style="position:absolute">
    <defs>
      <radialGradient id="xray-tone" cx="0.55" cy="0.75" r="0.8">
        <stop offset="0" stop-color="#36a6e6"/>
        <stop offset="0.45" stop-color="#1b48a8"/>
        <stop offset="1" stop-color="#0d1f5c"/>
      </radialGradient>
      <symbol id="phone" viewBox="0 0 24 20">
        <path d="M2 6c0-3 5-5 10-5s10 2 10 5v2h-5V6c-1-1-3-1.5-5-1.5S8 5 7 6v2H2z M6 9h12l3 9H3z M12 11a3 3 0 1 0 0.01 0z"/>
      </symbol>
    </defs>
  </svg>

  <!-- Flyer 2019 -->
  <article class="flyer flyer--2019">
    <svg class="flyer__shapes" viewBox="0 0 653 1304" preserveAspectRatio="none">
      <path class="shape-accent" d="M0,252 Q300,60 653,0 L653,420 L0,420 Z"/>
      <path class="shape-warm" d="M0,290 Q300,110 653,90 L653,420 L0,420 Z"/>
      <path role="img" aria-label="Röntgenartige Darstellung eines gebeugten Knies mit leuchtend hervorgehobenem Kniegelenk" fill="url(#xray-tone)" d="M0,318 Q300,50 653,207 L653,847 Q330,940 0,727 Z"/>
      <path class="shape-warm" d="M0,727 Q330,940 653,847 L653,905 Q330,960 0,897 Z"/>
      <path class="shape-accent" d="M0,897 Q330,960 653,905 L653,945 Q380,1085 0,1137 Z"/>
    </svg>
    <p class="flyer__date">21. – 23. Februar</p>
    <p class="flyer__year">2019</p>
    <h1 class="flyer__title">VELTRANA-<br>SYMPOSIUM</h1>
    <p class="flyer__topic">
      <span class="flyer__topic-lead">Neues aus der</span>
      <span class="flyer__topic-lead">Schulter- und Kniearthroskopie</span>
      <span class="flyer__venue">Krankenhaus Berlin</span>
    </p>
    <p class="flyer__body">Lorem ipsum dolor sit amet, consectetuer adipiscing elit. Aenean commodo ligula<br>eget dolor. Aenean massa. Cum sociis natoque penatibus et magnis dis parturient<br>montes, nascetur ridiculus mus. Donec quam felis, ultricies nec, pellentesque eu,</p>
    <p class="flyer__contact">ANMELDUNG UNTER: <svg class="flyer__phone-icon"><use href="#phone"/></svg><span class="flyer__phone">030. 555 41 26870</span></p>
    <div class="flyer__strip"></div>
  </article>

  <!-- Flyer 2020 -->
  <article class="flyer flyer--2020">
    <svg class="flyer__shapes" viewBox="0 0 653 1304" preserveAspectRatio="none">
      <path class="shape-accent" d="M0,252 Q300,60 653,0 L653,420 L0,420 Z"/>
      <path class="shape-warm" d="M0,290 Q300,110 653,90 L653,420 L0,420 Z"/>
      <path role="img" aria-label="Röntgenartige Darstellung zweier Füße mit leuchtend hervorgehobenem Sprunggelenk" fill="url(#xray-tone)" d="M0,318 Q300,50 653,207 L653,847 Q330,940 0,727 Z"/>
      <path class="shape-warm" d="M0,727 Q330,940 653,847 L653,905 Q330,960 0,897 Z"/>
      <path class="shape-accent" d="M0,897 Q330,960 653,905 L653,945 Q380,1085 0,1137 Z"/>
    </svg>
    <p class="flyer__date">21. – 23. Februar</p>
    <p class="flyer__year">2020</p>
    <h1 class="flyer__title">FUSSCHIRURGIE<br>KURS</h1>
    <p class="flyer__topic">
      <span class="flyer__topic-lead">Neues aus der</span>
      <span class="flyer__topic-lead">Schulter- und Kniearthroskopie</span>
      <span class="flyer__venue">Krankenhaus Berlin</span>
    </p>
    <p class="flyer__body">Lorem ipsum dolor sit amet, consectetuer adipiscing elit. Aenean commodo ligula<br>eget dolor. Aenean massa. Cum sociis natoque penatibus et magnis dis parturient<br>montes, nascetur ridiculus mus. Donec quam felis, ultricies nec, pellentesque eu.</p>
    <p class="flyer__contact">ANMELDUNG UNTER: <svg class="flyer__phone-icon"><use href="#phone"/></svg><span class="flyer__phone">030. 555 41 26870</span></p>
    <div class="flyer__strip"></div>
  </article>

</div>
</body>
</html>
```